Brenmoor Group needs a business card

I would like the card to be simple but modern and elegant.
I like black and white.
or black and gold.
we are a private finance lender and also are involved in property and property developments.

please look at the business card photos i provided i would like B.G only one one side and all the other details on the other side use fonts that tie in with my theme.

Industry/Entity Type

Finance

Contact Information for Business Card

Brenmoor Group (B.G) Callum Brenmoor M: 0418396152 E: callumbren@quivomail.com

Font styles to use
Other font styles liked:
• Use fonts that would reflect our business

Colors
000000
ffffff

Requirements
Must have
• one side of details
• other side has either B.G or Brenmoor Group like in the photos provided

```html
<!DOCTYPE html>
<html lang="en">
<head>
<meta charset="utf-8">
<title>Brenmoor Group — Business Card</title>
<link rel="stylesheet" href="https://fonts.googleapis.com/css2?family=Questrial&family=Oswald:wght@700&family=Open+Sans:wght@400&display=swap">
<style>
  :root {
    --ink: #000000;
    --paper: #ffffff;
    --backdrop: #2b2530;
    --card-shadow: rgba(0, 0, 0, 0.35);
  }
  * { margin: 0; padding: 0; box-sizing: border-box; }
  html, body {
    width: 1200px;
    height: 800px;
    overflow: hidden;
    background: var(--backdrop);
  }
  .canvas {
    position: relative;
    width: 1200px;
    height: 800px;
  }
  .card {
    position: absolute;
    top: 241px;
    width: 520px;
    height: 318px;
    box-shadow: 0 14px 30px var(--card-shadow);
    overflow: hidden;
  }
  .card--front { left: 50px; background: var(--paper); color: var(--ink); }
  .card--back  { left: 630px; background: var(--ink); color: var(--paper); }

  /* Front side */
  .accent-bar {
    position: absolute;
    left: 118px; top: 0;
    width: 18px; height: 108px;
    background: var(--ink);
  }
  .accent-notch {
    position: absolute;
    left: 142px; top: 0;
    width: 7px; height: 8px;
    background: var(--ink);
  }
  .holder-name {
    position: absolute;
    left: 48px; top: 116px;
    font-family: "Questrial", sans-serif;
    font-weight: 400;
    font-size: 26px;
    line-height: 32px;
    white-space: nowrap;
  }
  .holder-title {
    position: absolute;
    left: 40px; top: 152px;
    font-family: "Questrial", sans-serif;
    font-size: 10px;
    line-height: 14px;
  }
  .contact-rail {
    position: absolute;
    left: 0; top: 0;
    width: 520px; height: 318px;
  }
  .contact-item {
    position: absolute;
    left: 306px;
    font-family: "Open Sans", sans-serif;
    font-size: 11px;
    line-height: 16px;
    letter-spacing: 1px;
    white-space: nowrap;
  }
  .contact-item--phone { top: 182px; }
  .contact-item--email { top: 250px; }

  /* Back side */
  .brand {
    position: absolute;
    inset: 0;
    display: flex;
    flex-direction: column;
    align-items: center;
    justify-content: center;
    font-family: "Oswald", sans-serif;
    font-weight: 700;
    color: var(--paper);
    text-transform: uppercase;
  }
  .brand-initials {
    font-size: 96px;
    line-height: 1;
    letter-spacing: 2px;
  }
  .brand-name {
    font-size: 34px;
    line-height: 1.1;
    letter-spacing: 2px;
    margin-top: 2px;
  }
</style>
</head>
<body>
<main class="canvas">
  <section class="card card--front" aria-label="Business card front">
    <div class="accent-bar"></div>
    <div class="accent-notch"></div>
    <h1 class="holder-name">Callum Brenmoor</h1>
    <p class="holder-title">Postion/ Title</p>

    <svg class="contact-rail" viewBox="0 0 520 318" aria-hidden="true">
      <line x1="270" y1="166" x2="270" y2="318" stroke="#000" stroke-width="3"/>
      <circle class="phone-badge" cx="270" cy="190" r="22" fill="#000"/>
      <path d="M263 178 q-4 2 -3 8 q2 10 9 17 q5 4 9 1 l2 -2 l-5 -5 l-3 2 q-3 -2 -6 -7 q-2 -4 -1 -6 l3 -2 l-4 -7 z" fill="#fff"/>
      <circle class="mail-badge" cx="270" cy="258" r="22" fill="#000"/>
      <rect x="258" y="250" width="24" height="16" fill="none" stroke="#fff" stroke-width="2"/>
      <polyline points="258,250 270,260 282,250" fill="none" stroke="#fff" stroke-width="2"/>
    </svg>

    <p class="contact-item contact-item--phone">0418396152</p>
    <p class="contact-item contact-item--email">callumbren@quivomail.com</p>
  </section>

  <section class="card card--back" aria-label="Business card back">
    <div class="brand">
      <span class="brand-initials">B.G</span>
      <span class="brand-name">Brenmoor Group</span>
    </div>
  </section>
</main>
</body>
</html>
```